Asphalt Paving Specialists Business Cards

Our company is TREVIN ASPHALT. We need a business cards two of our asphalt paving team members. We're asphalt specialists.
I need two made up please. The details on the front of the each business card i would like please is as follows.
Address is 87 Marrowby St, Clontarf, QLD, 4019.

Company Director
Gordon Pelliway
gord@trevinpave.com.au
04 58 736 042
www.trevinpave.com.au

Supervisor
Curtis Vonnegard
curtis@trevinpave.com.au
0462 873 105
www.trevinpave.com.au

We do all aspects of Asphalt Paving. Specific Services include - Driveways, Carparks & sub-divisions. All Roads. Repairs and Maintenance.

We provide free quotes!

I dont have a certain way i want them to look so im open to all designs :)

** I have uploaded our logo for the TREVIN ASPHALT. HOWEVER, CAN YOU PLEASE GET RID OF THE ( PTY LTD )

Thank you
Renata Fulch
TREVIN ASPHALT

Target Market(s)

Home owners and Business Owners

Contact Information for Business Card

Asphalt Paving Specialists. All aspects of Asphalt. Residential, Commercial & Industrial. Based in Brisbane.

Font styles to use
Sans Serif

Colors

Designer to choose colors to be used in the design.

Requirements
Nice to have
• maybe an image of a driveway? or Asphalt?

```html
<!DOCTYPE html>
<html lang="en">
<head>
<meta charset="utf-8">
<title>Trevin Asphalt Business Cards</title>
<link rel="stylesheet" href="https://fonts.googleapis.com/css2?family=Open+Sans:wght@400;600;700&display=swap">
<style>
  :root {
    --backdrop: #2a2a2c;
    --card: #ffffff;
    --brand-blue: #1a9fdd;
    --ink: #1b1b1b;
    --rule: #222222;
  }
  * { box-sizing: border-box; margin: 0; padding: 0; }
  html, body {
    width: 1200px; height: 900px; overflow: hidden;
    background: var(--backdrop);
    font-family: "Open Sans", Arial, sans-serif;
  }
  .stage {
    width: 1200px; height: 900px;
    display: flex; flex-direction: column; align-items: center; justify-content: center;
    gap: 48px;
  }
  .card {
    width: 630px; height: 360px;
    background: var(--card);
    position: relative;
    box-shadow: 0 10px 28px rgba(0,0,0,.45);
  }
  .brand {
    display: flex; align-items: center; gap: 12px;
  }
  .brand-dot {
    width: 22px; height: 22px; border-radius: 50%;
    background: var(--brand-blue);
    flex: none;
  }
  .brand-name {
    font-weight: 700; color: var(--brand-blue);
    letter-spacing: 1px; white-space: nowrap;
  }

  /* services side */
  .card-services {
    display: flex; flex-direction: column; align-items: center; justify-content: center;
    text-align: center;
  }
  .card-services .brand-name { font-size: 40px; }
  .card-services .brand { margin-bottom: 26px; }
  .services-intro {
    color: var(--brand-blue); font-size: 16px; margin-bottom: 4px;
  }
  .services-list {
    color: var(--ink); font-weight: 700; font-size: 22px; line-height: 1.3;
    margin-bottom: 20px;
  }
  .services-offer {
    color: var(--brand-blue); font-weight: 700; font-size: 19px;
  }

  /* contact side */
  .card-contact {
    display: flex; align-items: center;
    padding: 0 40px 0 34px;
  }
  .card-contact .brand { width: 250px; }
  .card-contact .brand-name { font-size: 25px; }
  .divider {
    width: 2px; height: 170px; background: var(--rule);
    margin: 0 20px 0 14px; flex: none;
  }
  .contact-name {
    color: var(--brand-blue); font-weight: 700; font-size: 20px;
    text-transform: uppercase; letter-spacing: .3px; line-height: 1.1;
  }
  .contact-role {
    color: var(--ink); font-size: 16px; margin-bottom: 10px;
  }
  .contact-list { list-style: none; }
  .contact-list li {
    display: flex; align-items: flex-start; gap: 10px;
    color: var(--ink); font-size: 16px; line-height: 1.35;
  }
  .contact-list li.address { margin-top: 8px; }
  .contact-icon { width: 16px; height: 16px; flex: none; margin-top: 3px; }
  .contact-icon path, .contact-icon circle, .contact-icon rect { fill: var(--brand-blue); }
</style>
</head>
<body>
<main class="stage">

  <section class="card card-services">
    <div class="brand">
      <span class="brand-dot"></span>
      <span class="brand-name">TREVIN ASPHALT</span>
    </div>
    <p class="services-intro">We do all aspects of Asphalt Paving. Specific Services include</p>
    <p class="services-list">Driveways, Carparks &amp; sub-divisions<br>All Roads. Repairs and Maintenance.</p>
    <p class="services-offer">We provide free quotes!</p>
  </section>

  <section class="card card-contact">
    <div class="brand">
      <span class="brand-dot"></span>
      <span class="brand-name">TREVIN ASPHALT</span>
    </div>
    <div class="divider"></div>
    <div class="contact">
      <h2 class="contact-name">Gordon Pelliway</h2>
      <p class="contact-role">Company Director</p>
      <ul class="contact-list">
        <li>
          <svg class="contact-icon" viewBox="0 0 16 16" aria-hidden="true"><path d="M3.6 1l2.3 2.9-1.3 1.9c.9 2 2.6 3.7 4.6 4.6l1.9-1.3L14 11.4l-1.5 2.9C6.4 14 2 9.6 1.7 3.5z"/></svg>
          <span>04 58 736 042</span>
        </li>
        <li>
          <svg class="contact-icon" viewBox="0 0 16 16" aria-hidden="true"><path d="M1 3h14v1.2L8 9 1 4.2zM1 5.8l7 4.8 7-4.8V13H1z"/></svg>
          <span>gord@trevinpave.com.au</span>
        </li>
        <li>
          <svg class="contact-icon" viewBox="0 0 16 16" aria-hidden="true"><circle cx="8" cy="8" r="7"/><path d="M3 6h10v1H3zM3 9h10v1H3z" style="fill:#fff"/></svg>
          <span>www.trevinpave.com.au</span>
        </li>
        <li class="address">
          <svg class="contact-icon" viewBox="0 0 16 16" aria-hidden="true"><path d="M8 0a5.5 5.5 0 0 0-5.5 5.5C2.5 9.6 8 16 8 16s5.5-6.4 5.5-10.5A5.5 5.5 0 0 0 8 0zm0 7.6a2.1 2.1 0 1 1 0-4.2 2.1 2.1 0 0 1 0 4.2z"/></svg>
          <span>87 Marrowby St<br>Harlowe Bay, QLD, 4099</span>
        </li>
      </ul>
    </div>
  </section>

</main>
</body>
</html>
```